homepage design for online & live financial management course

homepage logo & required elements can be seen here -
http://kvt-portland.net/Index_new2011

we need a nice design to make it sing, and convert visitors to buyers

we like "Discover Hidden Profits in Your Business — Today!" but don't know how to incorporate it into the design

nice job! thanks for these submissions! keep it up -margaret @kvt/ledger summit (love the more elegant, simple lines of some of these!)

Industry/Entity Type

Financial

Requirements
Must have
• We need to have on the homepage -

- our logo (can not change) "Ledger Summit"
- our tag line (can not change) "Measure. Manage. Succeed."
- our 2-minute introductory video
- 2 options/buttons for visitor's next step: choose Online -or- Live

seen here -

```html
<!DOCTYPE html>
<html lang="en">
<head>
<meta charset="utf-8">
<title>Ledger Summit — Measure. Manage. Succeed.</title>
<link rel="stylesheet" href="https://fonts.googleapis.com/css2?family=Marcellus&family=Lora:ital,wght@1,700&display=swap">
<style>
  :root{
    --green:#2e7a60;
    --green-dark:#1b5843;
    --logo-green:#17654a;
    --ink-light:#f4f7f5;
    --orange:#d9700e;
    --footer:#050505;
  }
  *{box-sizing:border-box;margin:0;padding:0}
  html,body{width:1200px;height:946px;overflow:hidden}
  body{position:relative;background:var(--green);font-family:"Marcellus",serif;color:var(--ink-light)}
  .page{position:absolute;inset:0;overflow:hidden;
    background:radial-gradient(ellipse at 45% 55%,#378a6d 0%,var(--green) 55%,#226650 100%)}
  .header-bg{position:absolute;left:0;top:0;width:1200px;height:280px}
  .hero-photo{position:absolute;left:12px;top:0;width:306px;height:262px;
    background:radial-gradient(ellipse at 50% 45%,#cdb8a4 0%,#8b8a78 45%,#2a2a2a 100%);border-radius:0 0 30px 30px}
  .bags-photo{position:absolute;left:954px;top:36px;width:180px;height:204px;
    background:radial-gradient(ellipse at 50% 60%,#e2d0ad 0%,#c2a67a 60%,rgba(200,180,140,0) 100%)}
  .home-icon{position:absolute;left:1144px;top:16px;width:28px;height:28px}
  .logo-name{position:absolute;left:340px;top:74px;width:580px;text-align:center;
    font-family:"Marcellus",serif;font-size:60px;line-height:72px;color:var(--logo-green);white-space:nowrap}
  .tagline{position:absolute;left:342px;top:186px;width:576px;height:56px}
  .tagline-text{position:absolute;left:370px;top:188px;width:520px;height:40px;text-align:center;
    font-size:29px;line-height:40px;color:#fff;letter-spacing:.5px}
  .section-label{position:absolute;left:60px;top:282px;font-size:22px;color:#fff}
  .player{position:absolute;left:58px;top:324px;width:682px;height:410px;background:#111;border-radius:3px;padding:8px}
  .player-screen{width:666px;height:348px;
    background:radial-gradient(ellipse at 45% 45%,#ffffff 0%,#eeeeee 55%,#dcdcdc 100%)}
  .player-scene{position:absolute;left:66px;top:332px;width:666px;height:348px}
  .play-overlay{position:absolute;left:380px;top:480px}
  .controls{position:absolute;left:58px;top:690px;width:682px;height:44px;
    background:linear-gradient(#c7c9ca,#8d9092);border-radius:0 0 3px 3px}
  .ctrl-btn{position:absolute;top:6px;height:30px;border-radius:3px;
    background:linear-gradient(#e9eaea,#a9acad);border:1px solid #6d7072}
  .ctrl-play{left:10px;width:44px}
  .ctrl-vol{left:526px;width:40px}
  .ctrl-hd{left:576px;width:40px;font:italic 700 13px/28px Arial,sans-serif;color:#3c3f41;text-align:center}
  .ctrl-full{left:626px;width:40px}
  .track{position:absolute;left:84px;top:13px;width:322px;height:18px;border-radius:9px;
    background:repeating-linear-gradient(135deg,#6b6e70 0 3px,#5a5d5f 3px 6px);border:1px solid #3d4042}
  .track-buffer{position:absolute;left:0;top:0;width:182px;height:100%;border-radius:9px;
    background:repeating-linear-gradient(135deg,#9a9d9f 0 3px,#828587 3px 6px)}
  .track-played{position:absolute;left:0;top:0;width:76px;height:100%;border-radius:9px;background:linear-gradient(#7be08a,#22a03a)}
  .track-knob{position:absolute;left:66px;top:-1px;width:18px;height:18px;border-radius:50%;background:linear-gradient(#fff,#bbb);border:1px solid #777}
  .time{position:absolute;left:418px;top:13px;font:11px/18px Arial,sans-serif;color:#fff}
  .volume-pop{position:absolute;left:584px;top:584px;width:42px;height:100px;border-radius:4px;
    background:linear-gradient(#a7aaab,#6e7173);border:1px solid #4d5052}
  .volume-track{position:absolute;left:14px;top:10px;width:12px;height:80px;border-radius:6px;background:#2d3032}
  .volume-level{position:absolute;left:0;bottom:0;width:100%;height:60px;border-radius:6px;background:linear-gradient(90deg,#21a039,#7be08a)}
  .volume-knob{position:absolute;left:-3px;top:16px;width:18px;height:10px;border-radius:3px;background:linear-gradient(#fff,#bbb)}
  .side-panel{position:absolute;left:778px;top:256px;width:376px;height:474px;
    background:linear-gradient(#16523e,var(--green-dark) 70%,#246a51);border-radius:0 0 18px 18px}
  .choice{position:absolute;left:822px;width:284px;height:76px}
  .choice-online{top:332px}
  .choice-live{top:534px}
  .choice-btn{position:absolute;inset:0;border-radius:14px;
    background:linear-gradient(#fbfbfb 0%,#d7d8d9 45%,#a8abad 55%,#e3e4e5 100%);
    border:2px solid #8f9294;box-shadow:0 4px 8px rgba(0,0,0,.45);
    display:flex;flex-direction:column;align-items:center;justify-content:center;text-align:center;
    font-family:"Lora",serif;font-style:italic;font-weight:700;font-size:26px;line-height:29px;color:var(--orange);overflow:hidden}
  .choice-flag{position:absolute;right:-2px;top:-2px;width:56px;height:56px}
  .choice-note{position:absolute;left:778px;width:376px;text-align:center;font-size:22px;line-height:34px;color:#fff}
  .note-online{top:424px}
  .note-live{top:626px}
  .banner{position:absolute;left:56px;top:780px;width:1106px;height:54px;border-radius:6px;
    background:linear-gradient(#ffffff,#e4e5e5 60%,#cfd1d1);box-shadow:0 2px 5px rgba(0,0,0,.35);
    font-size:37px;line-height:54px;color:var(--logo-green);padding-left:30px;white-space:nowrap}
  .banner-bag{position:absolute;left:1002px;top:738px;width:108px;height:114px;border-radius:40% 40% 46% 46%;
    background:radial-gradient(ellipse at 50% 60%,#f4dc8a 0%,#d9b44e 60%,rgba(217,180,78,0) 100%)}
  .footer{position:absolute;left:0;top:898px;width:1200px;height:48px;background:var(--footer)}
  .social{position:absolute;left:64px;top:8px;display:flex;gap:10px}
  .social-dot{width:32px;height:32px;border-radius:50%;background:#6f7375}
  .copyright{position:absolute;right:54px;top:16px;font-family:"Marcellus",serif;font-size:13px;color:#fff}
</style>
</head>
<body>
<div class="page">
  <svg class="header-bg" viewBox="0 0 1200 280" aria-hidden="true">
    <defs>
      <linearGradient id="hdr" x1="0" y1="0" x2="0" y2="1">
        <stop offset="0" stop-color="#ffffff"/><stop offset="1" stop-color="#d6d7d7"/>
      </linearGradient>
    </defs>
    <path d="M0 0H1200V250Q600 280 0 250Z" fill="url(#hdr)"/>
  </svg>

  <div class="hero-photo" role="img" aria-label="Photo of a delighted woman holding fans of dollar bills"></div>
  <div class="bags-photo" role="img" aria-label="Photo of two burlap money bags marked with dollar signs"></div>

  <svg class="home-icon" viewBox="0 0 28 28" aria-label="Home">
    <path d="M14 3L2 14h4v11h7v-7h2v7h7V14h4z" fill="#2a2a2a"/>
  </svg>

  <h1 class="logo-name">Ledger Summit</h1>

  <svg class="tagline" viewBox="0 0 576 56" aria-hidden="true">
    <path d="M0 14H40V50H0L12 32Z" fill="#1f6a50"/>
    <path d="M576 14H536V50H576L564 32Z" fill="#1f6a50"/>
    <rect x="24" y="0" width="528" height="46" fill="#e8eeec"/>
    <rect x="28" y="2" width="520" height="40" fill="#1d6b50"/>
    <rect x="31" y="5" width="514" height="34" fill="none" stroke="#9fc5b6" stroke-width="1"/>
  </svg>
  <div class="tagline-text">Measure. Manage. Succeed</div>

  <div class="section-label">Video</div>

  <div class="player">
    <div class="player-screen"></div>
  </div>
  <div class="player-scene" role="img" aria-label="Video still: a golden dollar sign hatching from a cracked egg beside stacks of banknotes"></div>
  <svg class="play-overlay" width="36" height="40" viewBox="0 0 36 40" aria-label="Play video">
    <path d="M2 2L34 20L2 38Z" fill="#4a4a4a"/>
  </svg>

  <div class="controls">
    <div class="ctrl-btn ctrl-play">
      <svg width="44" height="28" viewBox="0 0 44 28"><path d="M17 8L29 14L17 20Z" fill="#3c3f41"/></svg>
    </div>
    <div class="track">
      <div class="track-buffer"></div>
      <div class="track-played"></div>
      <div class="track-knob"></div>
    </div>
    <div class="time">1:47 / 12:35</div>
    <div class="ctrl-btn ctrl-vol">
      <svg width="40" height="28" viewBox="0 0 40 28"><path d="M13 11h4l5-4v14l-5-4h-4z" fill="#3c3f41"/><path d="M25 10q3 4 0 8" stroke="#3c3f41" stroke-width="1.5" fill="none"/></svg>
    </div>
    <div class="ctrl-btn ctrl-hd">HD</div>
    <div class="ctrl-btn ctrl-full">
      <svg width="40" height="28" viewBox="0 0 40 28" fill="none" stroke="#3c3f41" stroke-width="2">
        <path d="M12 11V7h4M28 11V7h-4M12 17v4h4M28 17v4h-4"/>
      </svg>
    </div>
  </div>
  <div class="volume-pop">
    <div class="volume-track"><div class="volume-level"></div><div class="volume-knob"></div></div>
  </div>

  <div class="side-panel"></div>

  <div class="choice choice-online">
    <div class="choice-btn">Ledger Summit<br>Online</div>
    <svg class="choice-flag" viewBox="0 0 56 56" aria-hidden="true">
      <path d="M14 0H34L56 22V42Z" fill="#111"/>
      <text x="36" y="22" transform="rotate(45 36 22)" font-family="Arial,sans-serif" font-weight="700" font-size="9" fill="#fff" text-anchor="middle">NEW</text>
    </svg>
  </div>
  <p class="choice-note note-online">Instantly learn how to<br>unlock hidden profits</p>

  <div class="choice choice-live">
    <div class="choice-btn">Ledger Summit<br>Live</div>
    <svg class="choice-flag" viewBox="0 0 56 56" aria-hidden="true">
      <path d="M14 0H34L56 22V42Z" fill="#111"/>
      <text x="36" y="22" transform="rotate(45 36 22)" font-family="Arial,sans-serif" font-weight="700" font-size="9" fill="#fff" text-anchor="middle">NEW</text>
    </svg>
  </div>
  <p class="choice-note note-live">Learn about<br>in-person events</p>

  <div class="banner">Discover Hidden Profits in Your Business — Today!</div>
  <div class="banner-bag" role="img" aria-label="Illustration of a gold money bag with a dollar sign"></div>

  <footer class="footer">
    <div class="social">
      <span class="social-dot" role="img" aria-label="Social network link"></span>
      <span class="social-dot" role="img" aria-label="Social network link"></span>
      <span class="social-dot" role="img" aria-label="News feed link"></span>
      <span class="social-dot" role="img" aria-label="Photo sharing link"></span>
    </div>
    <p class="copyright">Copyright © 2011. www.ledgersummit.com</p>
  </footer>
</div>
</body>
</html>
```